Velmora Solutions Website Design

We are a B2B startup offering a free virtual data room and deal management platform for small businesses. We need a 10-page website geared towards business executives and entrepreneurs that is simple, uploads quickly and provides a good introduction to our product. We've attached a document setting forth the text of 8 of the 10 pages (the other two - Resources and Blog - need to be designed to allow the future posting of white papers and blog entries) and links to the screenshots and GIFs, all of which are in a folder on dropbox. We've also attached a zip file with our logo and a pdf file with our font and colors. Examples of websites we like include www.tarnwick.example, www.plovebar.example and https://brimlo.example.

Target Market(s)

Small business owners, business executives and entrepreneurs

Industry/Entity Type

Finance

Coding

Coded - Design and coding required

Number of Pages Required

5+ page

Font styles to use
Sans Serif

Colors
85abd2
f9ba93

Requirements
Must have
• Please use the Wordpress kestle theme I uploaded to code the site.
Nice to have
• Clean, uncluttered design. White background. Screenshots and gifs should be shown on monitors (desktop, laptop and iPad only). Blue and orange are our corporate colors, but you’re not limited to those two colors. See uploaded logo guide for complementary colors or use your own judgment.

```html
<!DOCTYPE html>
<html lang="en">
<head>
<meta charset="utf-8">
<title>Velmora – Workflow Management, Simplified</title>
<link href="https://fonts.googleapis.com/css2?family=Montserrat:wght@600;700;800&family=Lato:wght@400;700&display=swap" rel="stylesheet">
<style>
:root{
  --navy:#1d2b3a;
  --steel:#3f6480;
  --steel-dark:#2f4f67;
  --orange:#ec6d0e;
  --orange-soft:#f7c9b5;
  --sage:#dde8cc;
  --mist:#e9eef2;
  --band:#c8d6df;
  --text:#4a5560;
  --muted:#7d8791;
  --line:#d6dde3;
  --white:#ffffff;
}
*{box-sizing:border-box;margin:0;padding:0}
html,body{width:1200px;height:5233px;overflow:hidden;background:var(--white)}
body{position:relative;font-family:"Lato",Arial,sans-serif;color:var(--text)}
.abs{position:absolute}
h1,h2,h3,.brand{font-family:"Montserrat",Arial,sans-serif;color:var(--navy)}
.btn{display:inline-block;background:var(--orange);color:#fff;font-family:"Montserrat",Arial,sans-serif;font-weight:700;font-size:17px;letter-spacing:.5px;border-radius:30px;text-transform:uppercase;text-align:center;text-decoration:none;white-space:nowrap}
.circle{position:absolute;border-radius:50%}
.ring{position:absolute;border-radius:50%;border-style:solid}
.shot{position:absolute;background:linear-gradient(180deg,#eef1f4 0,#f6f7f9 100%);border:1px solid var(--line);box-shadow:0 4px 14px rgba(0,0,0,.08)}
.shot::before{content:"";position:absolute;left:0;top:0;right:0;height:7%;background:var(--steel-dark)}
.shot::after{content:"";position:absolute;left:0;top:7%;bottom:0;width:22%;background:#dfe5ea}
.dots{position:absolute;width:0;height:0}
.dots i{position:absolute;width:5px;height:5px;border-radius:50%;background:#cdd3d8}

/* header */
.site-header .brand{left:62px;top:26px;font-size:44px;font-weight:700;color:var(--steel-dark);letter-spacing:-1px}
.nav{left:560px;top:42px;display:flex;gap:26px;font-size:16px;color:var(--navy);white-space:nowrap}
.site-header .btn{left:962px;top:30px;width:160px;height:48px;line-height:48px;font-size:17px}

/* hero */
.hero h1{left:76px;top:236px;font-size:44px;line-height:56px;font-weight:700;color:var(--steel-dark);white-space:nowrap}
.hero p{left:76px;top:364px;width:480px;font-size:17px;line-height:26px;color:var(--navy)}
.hero .btn{left:76px;top:456px;width:185px;height:54px;line-height:54px}
.slider-dots{left:565px;top:714px;display:flex;gap:7px}
.slider-dots span{width:13px;height:13px;border-radius:50%;border:2px solid var(--steel)}
.slider-dots span.on{background:var(--steel)}

/* intro */
.intro h2{left:640px;top:830px;width:500px;font-size:38px;line-height:48px;font-weight:700}
.intro .lead{left:640px;top:942px;width:470px;font-size:15px;line-height:24px;color:var(--muted)}
.checks{left:640px;top:1048px;width:470px;list-style:none}
.checks li{position:relative;padding-left:38px;font-size:16px;line-height:24px;color:var(--navy);margin-bottom:14px}
.checks li svg{position:absolute;left:0;top:1px}
.video{left:640px;top:1318px;font-size:16px;color:var(--navy)}
.video strong{font-family:"Montserrat",Arial,sans-serif;font-size:20px;display:block;margin-bottom:4px}
.video a{color:var(--steel);text-decoration:underline}

/* features */
.features h2{left:0;width:1200px;top:1458px;text-align:center;font-size:40px;font-weight:700}
.features .sub{left:0;width:1200px;top:1517px;text-align:center;font-size:17px;color:var(--muted)}
.feature{position:absolute;width:330px;text-align:center}
.feature .icon{width:104px;height:104px;margin:0 auto 18px;border-radius:18px;display:flex;align-items:center;justify-content:center}
.feature h3{font-size:19px;font-weight:700;margin-bottom:10px}
.feature p{font-size:15px;line-height:23px;color:var(--muted)}

/* quote */
.quote{left:0;top:2188px;width:1200px;height:272px;background:var(--mist)}
.quote blockquote{position:absolute;left:0;width:1200px;top:82px;text-align:center;font-size:22px;line-height:32px;color:var(--navy)}
.quote cite{position:absolute;left:0;width:1200px;top:182px;text-align:center;font-style:normal;font-size:15px;font-weight:700;color:var(--steel-dark)}
.quote .mark{position:absolute;font-family:Georgia,serif;font-size:110px;color:#bcc8d1;line-height:1}

/* benefit rows */
.benefit h2{font-size:40px;font-weight:700;white-space:nowrap}
.benefit p{font-size:16px;line-height:25px;color:var(--muted)}

/* cta */
.cta{left:0;top:4607px;width:1200px;height:273px;background:var(--band)}
.cta h2{position:absolute;left:0;width:1200px;top:72px;text-align:center;font-size:38px;font-weight:700}
.cta p{position:absolute;left:0;width:1200px;top:126px;text-align:center;font-size:17px;color:var(--navy)}
.cta .btn{position:absolute;left:513px;top:172px;width:174px;height:54px;line-height:54px}

/* footer */
.footer .brand{left:70px;top:4934px;font-size:60px;font-weight:700;color:var(--steel-dark);letter-spacing:-2px}
.footer .social{left:168px;top:5020px;width:40px;height:40px;border-radius:50%;background:var(--steel)}
.fcol h4{font-family:"Montserrat",Arial,sans-serif;font-size:16px;font-weight:700;color:var(--steel-dark);margin-bottom:16px;letter-spacing:.5px}
.fcol ul{list-style:disc;padding-left:20px;font-size:15px;line-height:32px;color:var(--navy)}
.fcol p{font-size:14px;line-height:21px;color:var(--navy)}
.fcol .field{margin-top:14px;width:245px;height:38px;border:1px solid var(--line);border-radius:20px;font-size:13px;color:var(--muted);padding:10px 16px}
.fcol .btn{margin-top:14px;width:160px;height:44px;line-height:44px;font-size:16px}
.copyright{left:0;width:1200px;top:5195px;text-align:center;font-size:13px;color:var(--navy)}
</style>
</head>
<body>

<!-- header -->
<header class="site-header">
  <div class="abs brand">Velmora</div>
  <nav class="abs nav"><span>Features</span><span>Our Clients</span><span>Company</span><span>Contact Us</span></nav>
  <a class="abs btn">Try it now</a>
</header>

<!-- hero -->
<section class="hero">
  <div class="circle" style="left:150px;top:470px;width:120px;height:120px;background:var(--orange-soft);opacity:.7"></div>
  <div class="dots" style="left:270px;top:540px">
    <i style="left:0;top:0"></i><i style="left:18px;top:0"></i><i style="left:36px;top:0"></i><i style="left:54px;top:0"></i>
    <i style="left:0;top:18px"></i><i style="left:18px;top:18px"></i><i style="left:36px;top:18px"></i><i style="left:54px;top:18px"></i>
    <i style="left:0;top:36px"></i><i style="left:18px;top:36px"></i><i style="left:36px;top:36px"></i><i style="left:54px;top:36px"></i>
  </div>
  <div class="circle" style="left:960px;top:470px;width:330px;height:330px;background:var(--steel-dark)"></div>
  <div class="shot" style="left:680px;top:150px;width:520px;height:450px;border:12px solid #222;border-radius:14px 14px 0 0" role="img" aria-label="Laptop showing the Velmora workflow dashboard"></div>
  <div class="abs" style="left:640px;top:600px;width:560px;height:24px;background:linear-gradient(180deg,#cfd3d6,#9aa0a5);border-radius:0 0 18px 18px"></div>
  <h1 class="abs">Workflow Management,<br>Simplified</h1>
  <p class="abs">Simplify workflow management with Velmora – free business process management software built for collaboration and easy customization.</p>
  <a class="abs btn">Try it today</a>
  <div class="abs slider-dots"><span class="on"></span><span></span><span></span><span></span></div>
</section>

<!-- intro -->
<section class="intro">
  <div class="ring" style="left:-60px;top:830px;width:400px;height:400px;border-width:34px;border-color:var(--steel-dark)"></div>
  <div class="circle" style="left:330px;top:1210px;width:90px;height:90px;background:var(--sage)"></div>
  <div class="shot" style="left:100px;top:880px;width:460px;height:330px;border:12px solid #222;border-radius:12px 12px 0 0" role="img" aria-label="Laptop showing the Velmora document workspace"></div>
  <div class="abs" style="left:20px;top:1208px;width:600px;height:26px;background:linear-gradient(180deg,#d7dbde,#9aa0a5);border-radius:0 0 20px 20px"></div>
  <h2 class="abs">Manage Your Workflow Better with Velmora</h2>
  <p class="abs lead">The Velmora Assistant is a secure, sharable workflow management platform designed with your needs in mind. Here are some features you'll love:</p>
  <ul class="abs checks">
    <li><svg width="24" height="24" viewBox="0 0 24 24"><circle cx="12" cy="12" r="12" fill="#ec6d0e"/><path d="M7 12.5l3.2 3.2L17 9" stroke="#fff" stroke-width="2.4" fill="none" stroke-linecap="round"/></svg>Built for internal and external collaboration</li>
    <li><svg width="24" height="24" viewBox="0 0 24 24"><circle cx="12" cy="12" r="12" fill="#ec6d0e"/><path d="M7 12.5l3.2 3.2L17 9" stroke="#fff" stroke-width="2.4" fill="none" stroke-linecap="round"/></svg>Highly customizable and intuitive</li>
    <li><svg width="24" height="24" viewBox="0 0 24 24"><circle cx="12" cy="12" r="12" fill="#ec6d0e"/><path d="M7 12.5l3.2 3.2L17 9" stroke="#fff" stroke-width="2.4" fill="none" stroke-linecap="round"/></svg>Free to use – no setup or monthly</li>
    <li><svg width="24" height="24" viewBox="0 0 24 24"><circle cx="12" cy="12" r="12" fill="#ec6d0e"/><path d="M7 12.5l3.2 3.2L17 9" stroke="#fff" stroke-width="2.4" fill="none" stroke-linecap="round"/></svg>Free to use – no setup or monthly Fees.</li>
    <li><svg width="24" height="24" viewBox="0 0 24 24"><circle cx="12" cy="12" r="12" fill="#ec6d0e"/><path d="M7 12.5l3.2 3.2L17 9" stroke="#fff" stroke-width="2.4" fill="none" stroke-linecap="round"/></svg>If you want to process contracts faster while reducing costs (did we mention that it was free?), Velmora is the ideal solution for you.</li>
  </ul>
  <div class="abs video"><strong>Watch a Video :</strong><a>https://video.example/292822099</a></div>
</section>

<!-- features -->
<section class="features">
  <h2 class="abs">Features At-a-Glance</h2>
  <p class="abs sub">User-Friendly workflow management software that saves time and money</p>

  <div class="feature" style="left:51px;top:1596px">
    <div class="icon" style="background:var(--orange)"><svg width="56" height="56" viewBox="0 0 56 56" fill="none" stroke="#fff" stroke-width="3"><rect x="8" y="8" width="40" height="40" rx="4"/><path d="M16 20h24M16 28h24M16 36h14"/></svg></div>
    <h3>Workflow Management</h3>
    <p>Efficiently handle multi-party transactions with customizable, collaboration workflow software.</p>
  </div>
  <div class="feature" style="left:435px;top:1596px">
    <div class="icon" style="border:2px solid var(--line)"><svg width="56" height="56" viewBox="0 0 56 56" fill="none" stroke="#2f4f67" stroke-width="3"><rect x="12" y="6" width="32" height="44" rx="3"/><path d="M18 18l3 3 5-6M30 18h8M18 30l3 3 5-6M30 30h8M18 42h20"/></svg></div>
    <h3>Built-in Checklists</h3>
    <p>Swap old process checklists for online checklists linked to documents housed in our secure database</p>
  </div>
  <div class="feature" style="left:819px;top:1596px">
    <div class="icon" style="border:2px solid var(--line)"><svg width="56" height="56" viewBox="0 0 56 56" fill="none" stroke="#2f4f67" stroke-width="3"><path d="M16 38h26a9 9 0 0 0 0-18 13 13 0 0 0-25 2 8 8 0 0 0-1 16z"/><path d="M28 28v16M22 38l6 6 6-6"/></svg></div>
    <h3>Real-time Sharing</h3>
    <p>Automate new file requests and enable real-time downloads from a single self-service portal.</p>
  </div>
  <div class="feature" style="left:51px;top:1880px">
    <div class="icon" style="border:2px solid var(--line)"><svg width="56" height="56" viewBox="0 0 56 56" fill="none" stroke="#2f4f67" stroke-width="3"><circle cx="24" cy="24" r="14"/><path d="M34 34l12 12"/></svg></div>
    <h3>Better Transparency</h3>
    <p>Make all of your files visible to your team instantly from a secure, cloud-based sharing environment.</p>
  </div>
  <div class="feature" style="left:435px;top:1880px">
    <div class="icon" style="border:2px solid var(--line)"><svg width="56" height="56" viewBox="0 0 56 56" fill="none" stroke="#2f4f67" stroke-width="3"><path d="M34 16c-2-3-6-4-9-3s-5 4-3 7 12 4 13 9-3 8-8 8-8-2-9-5M28 8v40"/></svg></div>
    <h3>Lower Costs</h3>
    <p>Share your files from anywhere with anyone from a single, easy-to-use platform.</p>
  </div>
  <div class="feature" style="left:819px;top:1880px">
    <div class="icon" style="border:2px solid var(--line)"><svg width="56" height="56" viewBox="0 0 56 56" fill="none" stroke="#2f4f67" stroke-width="3"><path d="M28 6l18 7v13c0 12-8 20-18 24-10-4-18-12-18-24V13z"/><path d="M20 28l6 6 11-12"/></svg></div>
    <h3>End-to-end Security</h3>
    <p>Host your data on encrypted Nimbus servers complete with user authentication and tracking.</p>
  </div>
</section>

<!-- quote -->
<section class="abs quote">
  <span class="mark" style="left:262px;top:30px">“</span>
  <span class="mark" style="left:880px;top:100px">”</span>
  <blockquote>“Efficient workflow management has resulted in an 85% savings in deal<br>closings over the past six years.”</blockquote>
  <cite>— The Global Council for Contract Practice</cite>
</section>

<!-- waste less -->
<section class="benefit">
  <div class="dots" style="left:560px;top:2600px">
    <i style="left:0;top:0"></i><i style="left:20px;top:0"></i><i style="left:40px;top:0"></i><i style="left:60px;top:0"></i>
    <i style="left:0;top:20px"></i><i style="left:20px;top:20px"></i><i style="left:40px;top:20px"></i><i style="left:60px;top:20px"></i>
    <i style="left:0;top:40px"></i><i style="left:20px;top:40px"></i><i style="left:40px;top:40px"></i><i style="left:60px;top:40px"></i>
  </div>
  <div class="circle" style="left:530px;top:2860px;width:70px;height:70px;background:var(--sage)"></div>
  <div class="circle" style="left:605px;top:2880px;width:38px;height:38px;background:var(--orange-soft)"></div>
  <div class="shot" style="left:652px;top:2590px;width:548px;height:258px" role="img" aria-label="Screenshot of the Velmora workflow list view"></div>
  <h2 class="abs" style="left:78px;top:2668px">Waste Less, Do More</h2>
  <p class="abs" style="left:78px;top:2738px;width:460px">Reduce administrative costs by streamlining workflows and automating document storage and sharing from a single, cloud-based platform.</p>
</section>

<!-- simplify -->
<section class="benefit">
  <div class="ring" style="left:-120px;top:3300px;width:330px;height:330px;border-width:26px;border-color:var(--sage)"></div>
  <div class="shot" style="left:0;top:3090px;width:551px;height:348px" role="img" aria-label="Screenshot of the Velmora checklist templates"></div>
  <h2 class="abs" style="left:655px;top:3178px">Simplify Your Workflow</h2>
  <p class="abs" style="left:655px;top:3248px;width:470px">Manage your documents using visual cues and tools you're already familiar with – from process templates to customized checklists, reports on user activity, and more.</p>
</section>

<!-- communicate -->
<section class="benefit">
  <div class="ring" style="left:555px;top:3520px;width:260px;height:260px;border-width:18px;border-color:var(--mist)"></div>
  <div class="circle" style="left:560px;top:3860px;width:60px;height:60px;background:var(--orange-soft)"></div>
  <div class="shot" style="left:652px;top:3612px;width:548px;height:290px" role="img" aria-label="Screenshot of the Velmora shared documents portal"></div>
  <h2 class="abs" style="left:78px;top:3690px">Communicate Better</h2>
  <p class="abs" style="left:78px;top:3760px;width:460px">Share unlimited stored documents with your team and those outside your organization from an online portal with user permissions you define.</p>
</section>

<!-- keep customers -->
<section class="benefit">
  <div class="circle" style="left:120px;top:4020px;width:70px;height:70px;background:var(--orange-soft)"></div>
  <div class="ring" style="left:390px;top:4330px;width:200px;height:200px;border-width:20px;border-color:var(--mist)"></div>
  <div class="shot" style="left:0;top:4112px;width:551px;height:286px" role="img" aria-label="Screenshot of the Velmora client contact records"></div>
  <h2 class="abs" style="left:655px;top:4205px">Keep Customers Happy</h2>
  <p class="abs" style="left:655px;top:4275px;width:470px">Look up contract details, locate files, and share documents with a few clicks while providing a better customer experience.</p>
</section>

<!-- cta -->
<section class="abs cta">
  <h2>Manage Your Workflow with Velmora</h2>
  <p>Try it today. You'll wonder how you got by without it.</p>
  <a class="btn">Try it now</a>
</section>

<!-- footer -->
<footer class="footer">
  <div class="abs brand">Velmora</div>
  <div class="abs social"></div>
  <div class="abs fcol" style="left:345px;top:4930px">
    <h4>SITEMAP</h4>
    <ul><li>Features</li><li>Our Clients</li><li>Company</li><li>Contact Us</li></ul>
  </div>
  <div class="abs fcol" style="left:608px;top:4930px">
    <h4>QUICK LINKS</h4>
    <ul><li>End User Agreement</li><li>Terms of Service</li><li>Privacy Policy</li><li>Tutorial</li></ul>
  </div>
  <div class="abs fcol" style="left:875px;top:4930px;width:260px">
    <h4>NEWSLETTER</h4>
    <p>Would you like to receive our exclusive news and update ?</p>
    <div class="field">Enter Name *</div>
    <a class="btn">Subscribe</a>
  </div>
  <p class="abs copyright">©Velmora - 2018 All Right Reserved</p>
</footer>

</body>
</html>
```